Corvanta512 Business Card Redesign

I want to create a design for brand new business cards, I need something exceptional for clear plastic business card design. Please do not submit without it being on a clear design. Photos of the various logo versions attached.

```html
<!DOCTYPE html>
<html lang="en">
<head>
<meta charset="utf-8">
<title>Corvanta512 – Clear Business Card</title>
<link rel="stylesheet" href="https://fonts.googleapis.com/css2?family=Roboto:wght@400;500&display=swap">
<style>
  :root {
    --page-bg: #ecebe8;
    --page-shade: #d9d7d2;
    --card-tint-top: rgba(58, 78, 140, 0.55);
    --card-tint-bottom: rgba(30, 44, 96, 0.62);
    --card-edge: rgba(170, 186, 230, 0.7);
    --card-glint: rgba(255, 255, 255, 0.22);
    --gold: #d7ad52;
    --gold-soft: #e2bf6c;
  }
  * { margin: 0; padding: 0; box-sizing: border-box; }
  html, body {
    width: 1200px;
    height: 1044px;
    overflow: hidden;
    background: var(--page-bg);
  }
  .stage {
    width: 1200px;
    height: 1044px;
    display: flex;
    align-items: center;
    justify-content: center;
    background: radial-gradient(ellipse at 50% 45%, var(--page-bg) 0%, var(--page-shade) 100%);
  }
  .business-card {
    position: relative;
    width: 900px;
    height: 514px;
    border-radius: 6px;
    background:
      linear-gradient(125deg, var(--card-glint) 0%, rgba(255, 255, 255, 0) 38%),
      linear-gradient(170deg, var(--card-tint-top) 0%, var(--card-tint-bottom) 100%);
    border: 2px solid var(--card-edge);
    box-shadow:
      inset 0 0 0 1px rgba(255, 255, 255, 0.12),
      inset 0 0 40px rgba(200, 215, 255, 0.12),
      0 22px 40px rgba(30, 40, 70, 0.12);
    display: flex;
    flex-direction: column;
    align-items: center;
    padding-top: 176px;
    font-family: "Roboto", Arial, sans-serif;
    color: var(--gold);
    text-align: center;
  }
  .brand-lockup {
    display: flex;
    align-items: center;
    gap: 16px;
    margin-bottom: 46px;
  }
  .brand-dot {
    width: 26px;
    height: 26px;
    border-radius: 50%;
    background: var(--gold);
  }
  .brand-name {
    font-size: 52px;
    font-weight: 500;
    letter-spacing: 1px;
    color: var(--gold);
  }
  .contact-name {
    font-size: 31px;
    font-weight: 500;
    color: var(--gold-soft);
    margin-bottom: 10px;
  }
  .contact-line {
    font-size: 28px;
    font-weight: 400;
    color: var(--gold-soft);
    line-height: 1.36;
  }
</style>
</head>
<body>
  <main class="stage">
    <section class="business-card">
      <div class="brand-lockup">
        <span class="brand-dot"></span>
        <span class="brand-name">Corvanta512</span>
      </div>
      <p class="contact-name">Marlo Trent, Attorney at Law</p>
      <p class="contact-line">555-0148</p>
      <p class="contact-line">marlo.trent@corvanta512.com</p>
      <p class="contact-line">www.corvanta512.com</p>
    </section>
  </main>
</body>
</html>
```